Corvane Property Group Business cards

I am starting a property development and consultancy business called Corvane Property Group. I have a logo designed and a website on its way:
www.corvanegroup-example.com.au

I need a business card with the following:

Front:
Mostly orange with logo taking up all front of card

Back of card:
Logo

Mark Dellaway
Managing Director

T +61 452 907 364
E mark.dellaway@corvanegroup-example.com.au
www.corvanegroup-example.com.au

Industry/Entity Type

Business

Requirements
Must have
• curved edges

```html
<!DOCTYPE html>
<html lang="en">
<head>
<meta charset="utf-8">
<title>Corvane Property Group – Business Cards</title>
<link rel="stylesheet" href="https://fonts.googleapis.com/css2?family=Roboto:wght@300;400;500;700&display=swap">
<style>
  :root {
    --stage: #2b2b2b;
    --brand-yellow: #fdcb35;
    --charcoal: #2a2a2a;
    --card-white: #f7f7f7;
    --ink: #333333;
    --ink-soft: #555555;
    --rule: #9a9a9a;
    --white: #ffffff;
  }
  * { box-sizing: border-box; margin: 0; padding: 0; }
  html, body {
    width: 1200px; height: 900px; overflow: hidden;
    background: var(--stage);
    font-family: "Roboto", Arial, sans-serif;
  }
  .canvas {
    position: relative; width: 1200px; height: 900px;
  }
  .card {
    position: absolute; left: 260px;
    width: 680px; height: 380px;
    border-radius: 14px; overflow: hidden;
  }

  /* Back of card – contact side */
  .card-back { top: 55px; background: var(--card-white); }
  .card-back .brand-block {
    position: absolute; left: 0; top: 150px;
    width: 270px; height: 150px;
    background: var(--brand-yellow);
    display: flex; flex-direction: column; justify-content: flex-end;
    padding: 0 0 18px 22px;
  }
  .brand-name {
    color: var(--white); font-weight: 300; line-height: 1;
  }
  .card-back .brand-name .word-main { font-size: 50px; letter-spacing: 1px; display: block; }
  .card-back .brand-name .word-sub { font-size: 16px; letter-spacing: 3px; display: block; margin-top: 6px; }
  .card-back .divider {
    position: absolute; left: 300px; top: 70px;
    width: 1px; height: 180px; background: var(--rule);
  }
  .contact { position: absolute; left: 325px; top: 70px; right: 20px; }
  .contact .person-name { font-size: 30px; font-weight: 500; color: var(--ink); }
  .contact .person-role { font-size: 17px; font-weight: 500; color: var(--ink-soft); margin-top: 4px; }
  .contact-list { list-style: none; margin-top: 24px; }
  .contact-list li {
    display: flex; align-items: center; gap: 10px;
    font-size: 13px; color: var(--ink-soft); margin-bottom: 10px;
  }
  .contact-list .icon {
    width: 20px; height: 20px; flex: none;
    background: var(--charcoal); border-radius: 3px;
    display: flex; align-items: center; justify-content: center;
  }

  /* Front of card – brand side */
  .card-front { top: 465px; background: var(--charcoal); }
  .card-front .yellow-band {
    position: absolute; left: 0; top: 0; width: 100%; height: 200px;
    background: var(--brand-yellow);
  }
  .card-front .brand-name {
    position: absolute; left: 110px; top: 95px;
  }
  .card-front .brand-name .word-main { font-size: 112px; letter-spacing: 2px; display: block; }
  .card-front .brand-name .word-sub { font-size: 30px; letter-spacing: 8px; display: block; margin-top: 8px; }
  .card-front .web {
    position: absolute; left: 0; right: 0; top: 300px;
    text-align: center; color: var(--brand-yellow);
    font-size: 20px; font-weight: 500; letter-spacing: 2px;
  }
</style>
</head>
<body>
<main class="canvas">

  <section class="card card-back" aria-label="Business card back">
    <div class="brand-block">
      <p class="brand-name"><span class="word-main">CORVANE</span><span class="word-sub">PROPERTY GROUP</span></p>
    </div>
    <div class="divider"></div>
    <div class="contact">
      <h1 class="person-name">Mark Dellaway</h1>
      <p class="person-role">Managing Director</p>
      <ul class="contact-list">
        <li>
          <span class="icon"><svg width="12" height="12" viewBox="0 0 24 24"><path fill="#fff" d="M6.6 10.8a15 15 0 0 0 6.6 6.6l2.2-2.2c.3-.3.7-.4 1-.2 1.1.4 2.3.6 3.6.6.6 0 1 .4 1 1V20c0 .6-.4 1-1 1A17 17 0 0 1 3 4c0-.6.4-1 1-1h3.5c.6 0 1 .4 1 1 0 1.3.2 2.5.6 3.6.1.3 0 .7-.2 1z"/></svg></span>
          +61 452 907 364
        </li>
        <li>
          <span class="icon"><svg width="12" height="12" viewBox="0 0 24 24"><rect x="2" y="5" width="20" height="14" rx="2" fill="#fff"/><path d="M3 6l9 7 9-7" stroke="#2a2a2a" stroke-width="2" fill="none"/></svg></span>
          mark.dellaway@corvanegroup-example.com.au
        </li>
        <li>
          <span class="icon"><svg width="12" height="12" viewBox="0 0 24 24" fill="none" stroke="#fff" stroke-width="2"><circle cx="12" cy="12" r="9"/><ellipse cx="12" cy="12" rx="4" ry="9"/><path d="M3 12h18"/></svg></span>
          www.corvanegroup-example.com.au
        </li>
      </ul>
    </div>
  </section>

  <section class="card card-front" aria-label="Business card front">
    <div class="yellow-band"></div>
    <p class="brand-name"><span class="word-main">CORVANE</span><span class="word-sub">PROPERTY GROUP</span></p>
    <p class="web">www.corvanegroup-example.com.au</p>
  </section>

</main>
</body>
</html>
```